Chewing Gum With Active Ingredients Needs Packaging Design

Brivelle Gum Science is a revolutionary new chewing gum that contains active ingredients commonly found in mouthwashes - it's a portable and convenient way to keep a fresh, clean, and healthy mouth. We have a thorough design brief (attached file) for the packaging we need - a simple sleeve for blister packed gum. We want our design to convey that we are a modern, effective, and high-end product.

Target Market(s)

Young professionals, 20-35 years old

Font styles to use
Serif
Sans Serif

Colors
0292cd
ffffff
0555a3

Requirements
Must have
• A sleek, elegant design
• ALL of the elements listed in the creative brief PDF
• Attached logo
Nice to have
• Incorporation of foil into the design
• A unique, unmistakable look
Should not have
• Too medical of a look

```html
<!DOCTYPE html>
<html lang="en">
<head>
<meta charset="utf-8">
<title>Brivelle Gum Science – Peppermint Sleeve</title>
<link rel="stylesheet" href="https://fonts.googleapis.com/css2?family=Raleway:wght@300;400;600;700&display=swap">
<style>
  :root {
    --canvas: #ffffff;
    --sleeve: #141414;
    --sleeve-top: #050505;
    --facet: #2a2a2a;
    --ink: #ffffff;
    --brand-deep: #2e2c8c;
    --brand-mid: #0555a3;
    --brand-bright: #0292cd;
    --gum: #8fb59b;
    --foil: #a9aaa8;
  }
  * { margin: 0; padding: 0; box-sizing: border-box; }
  html, body {
    width: 1200px; height: 1200px; overflow: hidden;
    background: var(--canvas);
    font-family: "Raleway", sans-serif;
  }
  .sleeve {
    position: absolute;
    left: 155px; top: 362px;
    width: 890px; height: 476px;
    background: var(--sleeve);
    color: var(--ink);
    overflow: hidden;
  }
  .sleeve__top-fold {
    position: absolute; left: 0; top: 0; width: 100%; height: 24px;
    background: var(--sleeve-top);
  }
  .sleeve__facets {
    position: absolute; left: 0; top: 24px; width: 100%; height: 410px;
    background:
      radial-gradient(ellipse at 20% 20%, rgba(60,60,60,.55), transparent 55%),
      radial-gradient(ellipse at 75% 65%, rgba(60,60,60,.5), transparent 55%),
      radial-gradient(ellipse at 95% 15%, rgba(55,55,55,.45), transparent 40%);
  }
  .brand {
    position: absolute; left: 0; width: 100%; top: 48px;
    display: flex; flex-direction: column; align-items: center;
  }
  .brand__dot {
    width: 70px; height: 70px; border-radius: 50%;
    border: 4px solid var(--brand-mid);
  }
  .brand__name {
    margin-top: 14px;
    font-weight: 300; font-size: 20px; letter-spacing: 7px;
    text-transform: uppercase;
    color: var(--brand-bright);
  }
  .claims-top {
    position: absolute; right: 38px; top: 42px; width: 140px;
    text-align: center; font-size: 11px; font-weight: 400; line-height: 1.15;
    text-transform: uppercase;
  }
  .count {
    position: absolute; left: 20px; top: 397px;
    font-size: 13.5px; line-height: 1.05; text-transform: uppercase;
  }
  .count strong { display: block; padding-left: 32px; font-weight: 700; }
  .count span { font-weight: 400; }
  .flavour {
    position: absolute; right: 16px; top: 411px;
    font-size: 13.5px; font-weight: 700; text-transform: uppercase;
  }
  .benefits {
    position: absolute; left: 0; bottom: 0; width: 100%; height: 42px;
    background: linear-gradient(90deg, var(--brand-deep), var(--brand-mid) 45%, var(--brand-bright));
    display: flex; align-items: center; justify-content: center; gap: 12px;
    font-size: 14px; font-weight: 400; text-transform: uppercase; letter-spacing: .2px;
  }
  .benefits .sep { font-size: 10px; }
  .window {
    position: absolute; left: 822px; top: 162px; width: 90px; height: 142px;
    border-radius: 14px 0 0 14px;
    background: linear-gradient(180deg, var(--brand-bright), var(--brand-deep));
    padding: 10px 0 10px 10px;
  }
  .window__view {
    width: 100%; height: 100%; border-radius: 8px 0 0 8px;
    background: linear-gradient(180deg, var(--gum), var(--foil) 50%, var(--gum));
  }
</style>
</head>
<body>
  <section class="sleeve">
    <div class="sleeve__top-fold"></div>
    <div class="sleeve__facets" role="img" aria-label="Dark faceted low-poly triangle pattern"></div>

    <div class="brand">
      <div class="brand__dot"></div>
      <div class="brand__name">Brivelle Gum Science</div>
    </div>

    <p class="claims-top">Aspartame free<br>with xylitol</p>

    <div class="window">
      <div class="window__view" role="img" aria-label="Window showing green gum pieces in the foil blister"></div>
    </div>

    <p class="count"><strong>8 pieces</strong><span>Sugar free gum</span></p>
    <p class="flavour">Peppermint</p>

    <div class="benefits">
      <span>Whitens teeth</span><span class="sep">•</span>
      <span>Freshens breath</span><span class="sep">•</span>
      <span>Helps reduce plaque</span><span class="sep">•</span>
      <span>Helps protect gums</span>
    </div>
  </section>
</body>
</html>
```